small auto electrical company needs new logo and business cards !!!

we are a small auto electrical company (Corvanne Motors Ltd) that has been running for 13 years the logo we have was put together by dinosaurs so we are looking at re branding the company starting with business cards and a new logo we fit GPS tracking devices for young drivers through there insurance company also we fit hands free systems and dash cameras also safety locks to fleet vehicles we would like bright eye catching colours day glow and neon and quirky designs for the logo our original logo was baby blue which i have added a picture enclosed we would like double sided but have a space to write notes and prices preferably not white on back same colour throughout many thanks
Reason: Just a chance to finalise any designs we want CM logos or C logos - No 1st's and no dinosaurs lol
Industry/Entity Type
Business
Contact Information for Business Card
Installs@corvannemotors.co.uk
07700900482
www.Corvannemotors.co.uk
Logo Text
Corvanne Motors Ltd - Fleets and Insurance Services
Requirements
Must have
- new logo design !!
Nice to have
- Satellite in logo or something attaining to gps
- maybe a car in the logo
Should not have
- shouldnt have first as 1st it is CoRVANNE Motors

```html
<!DOCTYPE html>
<html lang="en">
<head>
<meta charset="utf-8">
<title>Corvanne Motors Ltd – Business Card</title>
<link href="https://fonts.googleapis.com/css2?family=Questrial&family=Oswald:wght@500&display=swap" rel="stylesheet">
<style>
  :root {
    --backdrop: #6d6e70;
    --card-purple: #682a6c;
    --swoosh-white: #ffffff;
    --swoosh-grey: #b9b9bd;
    --swoosh-dark: #0c0c0c;
    --accent-orange: #f0532b;
    --service-green: #8dc63f;
    --badge-blue: #1f80c6;
    --badge-yellow: #f4e83a;
    --logo-blue: #4fc6f2;
    --faint-circle: #6a6aa0;
    --contact-yellow: #f3e834;
    --icon-green: #6cbf45;
  }
  * { margin: 0; padding: 0; box-sizing: border-box; }
  html, body { width: 1200px; height: 900px; overflow: hidden; background: var(--backdrop); }
  .canvas { position: relative; width: 1200px; height: 900px; }
  .card {
    position: absolute; width: 506px; height: 288px; overflow: hidden;
    background: var(--card-purple);
    font-family: "Questrial", "Century Gothic", sans-serif;
  }
  .card--front { left: 357px; top: 93px; }
  .card--back { left: 342px; top: 492px; }
  .swoosh { position: absolute; left: 0; width: 506px; }
  .swoosh--top { top: 0; height: 90px; }
  .swoosh--bottom { bottom: 0; height: 90px; }

  .brand-mini {
    position: absolute; right: 12px; top: 8px;
    display: flex; align-items: center; gap: 5px;
    font-family: "Oswald", sans-serif; font-weight: 500;
    font-size: 12px; letter-spacing: 0.5px; color: var(--logo-blue);
    white-space: nowrap;
  }
  .brand-mini__dot { width: 20px; height: 20px; border-radius: 50%; background: var(--logo-blue); }

  .offer-title {
    position: absolute; left: 38px; top: 76px;
    font-size: 39px; font-weight: 400; color: var(--accent-orange); line-height: 1;
    white-space: nowrap;
  }
  .service-list { position: absolute; left: 40px; top: 138px; list-style: none; }
  .service-list li {
    display: flex; align-items: center; gap: 8px;
    font-size: 25px; line-height: 28px; color: var(--service-green);
    white-space: nowrap;
  }
  .service-list li::before {
    content: ""; width: 13px; height: 13px; border-radius: 50%;
    background: var(--accent-orange); flex: none;
  }
  .experience-badge {
    position: absolute; left: 333px; top: 93px; width: 155px; height: 63px;
    background: var(--badge-blue); border-radius: 7px;
    box-shadow: 0 0 12px 3px rgba(120, 200, 255, 0.55);
    color: var(--badge-yellow); text-align: center;
    display: flex; flex-direction: column; justify-content: center;
    white-space: nowrap;
  }
  .experience-badge__years { font-size: 27px; line-height: 27px; }
  .experience-badge__label { font-size: 20px; line-height: 22px; }

  .faint-circle {
    position: absolute; left: 0; top: 0; width: 232px; height: 232px;
    border-radius: 50%; background: var(--faint-circle);
  }
  .brand {
    position: absolute; left: 255px; top: 18px; width: 245px;
    font-family: "Oswald", sans-serif; font-weight: 500; color: var(--logo-blue);
    white-space: nowrap;
  }
  .brand__dot {
    width: 76px; height: 76px; border-radius: 50%; background: var(--logo-blue);
    margin-left: 73px;
  }
  .brand__name { margin-top: 10px; font-size: 23px; line-height: 30px; letter-spacing: 1px; }
  .brand__tagline { font-size: 16px; line-height: 20px; letter-spacing: 1.2px; }

  .contact {
    position: absolute; display: flex; align-items: center; gap: 12px;
    color: var(--contact-yellow); font-size: 13px; line-height: 19px; white-space: nowrap;
  }
  .contact--web { left: 21px; top: 190px; }
  .contact--phone { left: 286px; top: 190px; }
  .contact__icon { width: 40px; height: 40px; border-radius: 4px; background: var(--icon-green); flex: none; }
</style>
</head>
<body>
<main class="canvas">

  <section class="card card--front" aria-label="Business card front">
    <svg class="swoosh swoosh--top" viewBox="0 0 506 90" aria-hidden="true">
      <defs>
        <linearGradient id="frontDark" x1="0" x2="1">
          <stop offset="0.55" stop-color="#ffffff"/>
          <stop offset="0.85" stop-color="#8a8a8e"/>
          <stop offset="1" stop-color="#0c0c0c"/>
        </linearGradient>
      </defs>
      <path d="M0 0H506V62C420 40 330 44 250 50C150 58 70 62 0 44Z" fill="var(--swoosh-grey)"/>
      <path d="M0 0H506V50C420 28 330 32 250 38C150 46 70 48 0 34Z" fill="url(#frontDark)"/>
    </svg>
    <div class="brand-mini"><span class="brand-mini__dot"></span>CORVANNE MOTORS LTD</div>

    <h2 class="offer-title">We offer to fit</h2>
    <ul class="service-list">
      <li>GPS tracking devices</li>
      <li>Hands free systems</li>
      <li>Dash cameras</li>
      <li>Safety locks</li>
    </ul>
    <div class="experience-badge">
      <span class="experience-badge__years">13 YEARS</span>
      <span class="experience-badge__label">EXPERIENCE</span>
    </div>
  </section>

  <section class="card card--back" aria-label="Business card back">
    <div class="faint-circle" aria-hidden="true"></div>
    <div class="brand">
      <div class="brand__dot" aria-hidden="true"></div>
      <div class="brand__name">CORVANNE MOTORS LTD</div>
      <div class="brand__tagline">FLEET &amp; INSURANCE SERVICE</div>
    </div>

    <div class="contact contact--web">
      <svg class="contact__icon" viewBox="0 0 40 40" aria-hidden="true">
        <rect width="40" height="40" rx="4" fill="var(--icon-green)"/>
        <g fill="none" stroke="#fff" stroke-width="2">
          <circle cx="20" cy="20" r="11"/>
          <ellipse cx="20" cy="20" rx="5" ry="11"/>
          <path d="M9 20H31M11 14H29M11 26H29"/>
        </g>
      </svg>
      <div>Installs@corvannemotors.co.uk<br>www.Corvannemotors.co.uk</div>
    </div>
    <div class="contact contact--phone">
      <svg class="contact__icon" viewBox="0 0 40 40" aria-hidden="true">
        <rect width="40" height="40" rx="4" fill="var(--icon-green)"/>
        <path d="M13 10l5 0 2 6-3 2c1.5 3 3.5 5 6 6l2-3 6 2 0 5c-1 1-3 2-5 1.5C17 27 12 22 10 15c-.5-2 .5-4 3-5z" fill="#fff"/>
      </svg>
      <div>+44 07700900482</div>
    </div>

    <svg class="swoosh swoosh--bottom" viewBox="0 0 506 90" aria-hidden="true">
      <defs>
        <linearGradient id="backDark" x1="0" x2="1">
          <stop offset="0.5" stop-color="#ffffff"/>
          <stop offset="0.82" stop-color="#8a8a8e"/>
          <stop offset="1" stop-color="#0c0c0c"/>
        </linearGradient>
      </defs>
      <path d="M0 52C80 62 170 46 260 38C360 28 440 26 506 40V90H0Z" fill="var(--swoosh-grey)"/>
      <path d="M0 62C80 72 170 58 260 50C360 40 440 40 506 52V90H0Z" fill="url(#backDark)"/>
    </svg>
  </section>

</main>
</body>
</html>
```